Association qui souhaite améliorer l'accès aux personnes en situation de handicap

Nous sommes une association qui a pour objectif d'améliorer l'accessibilité, augmenter l'offre des activités réalisables dans notre région touristique.
Nous souhaitons réaliser un site internet afin de pouvoir communiquer sur notre association. Nous avons déjà conçu notre flyer sur Graphivolta. Nous souhaiterions une base graphique se rapportant à celui-ci. C'est possible de tout retravailler mais nous souhaitons tout de même retrouver la charte graphique ou code couleur du flyer.
Il nous faudrait quelques pages:
- 1 page : Acceuil / Présentation (Home), Il y aurait le descriptif de l'association, avec ses objectifs à +/- moyen terme
- 1 page : Nos réalisations, celle-ci présenterait les éléments que nous avons réalisés avec des zones de textes et des images classées chronologiquement au fur et à mesure des nouveautés
- 1 page : Media, comme la précédente, mais ou on pourrait voir ou lire sur les divers médias qui parlent de nous
- 1 page : Evenements : c'est une page pour présenter divers activités que nous allons organiser
- 1 page : Contact qui indique comment nous contacter et avec la présentation des 5 ou 6 membres du comité
- 1 link donate : qui arrive sur un formulaire de donnée que l'on pourra faire évoluer sur un système de payement par la suite. Cette bannière doit se retrouver sur toutes les pages
Il est nécessaire que se design puisse être transféré sur une lecture sur téléphone mobile
Target Market(s)
Personnes en situation de handicap
Industry/Entity Type
Associatif
Coding
Coded - Design and coding required
Number of Pages Required
5+ page

```html
<!DOCTYPE html>
<html lang="en">
<head>
<meta charset="utf-8">
<title>Pasrel Collective</title>
<link href="https://fonts.googleapis.com/css2?family=Poppins:wght@400;500;600;700;800&family=Roboto:wght@400;500;700&display=swap" rel="stylesheet">
<style>
:root{
  --red:#b5091c;
  --ink:#1b1b1b;
  --slate:#2f3538;
  --sky:#e3f4fb;
  --blush:#f8e8e9;
  --text:#3c3c3c;
  --white:#ffffff;
  --black:#050505;
}
*{box-sizing:border-box;margin:0;padding:0}
html,body{width:1200px;height:4559px;overflow:hidden}
body{position:relative;font-family:"Roboto",sans-serif;color:var(--text);background:var(--white)}
.abs{position:absolute}
.btn{position:absolute;display:flex;align-items:center;justify-content:center;background:var(--red);color:var(--white);font-family:"Poppins",sans-serif;font-weight:700;border-radius:20px;text-transform:uppercase}
.section-title{position:absolute;left:0;width:1200px;text-align:center;font-family:"Poppins",sans-serif;font-weight:700;font-size:29px;color:var(--ink);text-transform:uppercase}
.section-title::after{content:"";display:block;width:100px;height:3px;background:var(--red);margin:16px auto 0}

/* hero */
.hero-photo{left:0;top:0;width:1200px;height:790px;background:linear-gradient(180deg,#1f6fb3 0%,#4a9ad3 38%,#9fc7d8 52%,#5f7a3a 60%,#3d5b22 80%,#2e4516 100%)}
.site-nav{left:0;top:0;width:1200px;height:140px}
.brand{left:110px;top:52px;font-family:"Poppins",sans-serif;font-weight:700;color:var(--white);font-size:17px;line-height:19px;text-transform:uppercase;display:flex;align-items:center;gap:10px}
.brand-mark{width:34px;height:34px;background:var(--red);border-radius:50%}
.nav-links{left:487px;top:64px;display:flex;gap:35px;font-size:15px;color:var(--white)}
.nav-links .active{border-bottom:2px solid var(--red);padding-bottom:4px}
.nav-contact{left:961px;top:56px;width:126px;height:36px;font-size:15px;text-transform:none}
.hero-title{left:112px;top:210px;font-family:"Poppins",sans-serif;font-weight:800;font-size:39px;line-height:48px;color:var(--white);text-transform:uppercase}
.hero-text{left:110px;top:320px;width:560px;font-size:14.5px;line-height:24px;color:#eef4fb}
.hero-donate{left:112px;top:388px;width:125px;height:36px;font-size:14px}

/* about */
.about-bg{left:0;top:780px;width:1200px;height:470px}
.about-title{left:110px;top:885px;font-family:"Poppins",sans-serif;font-weight:700;font-size:29px;color:var(--red)}
.about-lead{left:110px;top:932px;width:425px;font-size:20px;line-height:29px;color:var(--ink);text-align:justify}
.about-lead::after{content:"";display:block;width:100px;height:3px;background:var(--red);margin-top:12px}
.about-text{left:598px;top:888px;width:490px;font-size:15px;line-height:23px;text-align:justify;color:var(--text)}
.about-more{left:600px;top:1048px;width:126px;height:36px;font-size:14px}

/* achievements */
.achievement{width:240px;text-align:center}
.achievement .icon{width:140px;height:140px;border-radius:50%;margin:0 auto;display:flex;align-items:center;justify-content:center}
.achievement .icon.dark{background:var(--slate)}
.achievement .icon.red{background:var(--red)}
.achievement h3{font-family:"Poppins",sans-serif;font-weight:600;font-size:18px;color:var(--ink);margin-top:16px}
.achievement p{font-size:12.5px;line-height:19px;color:var(--text);margin:10px auto 0;width:195px}

/* media */
.media-bg{left:0;top:1828px;width:1200px;height:550px;background:var(--blush)}
.media-card{top:2027px;width:304px;height:233px;border:5px solid var(--white);box-shadow:0 4px 14px rgba(0,0,0,.12)}
.media-photo{width:100%;height:100%;background:linear-gradient(160deg,#2b2326 0%,#8a1f24 45%,#c92a2f 70%,#3a2b2c 100%)}
.media-photo.street{background:linear-gradient(180deg,#5f8a57 0%,#a33a3a 40%,#c52b2e 62%,#2c2a2c 100%)}
.media-feature{background:linear-gradient(160deg,#c41f2b,#a3101e);color:var(--white);text-align:center;padding:40px 26px 0}
.media-feature h4{font-family:"Poppins",sans-serif;font-weight:700;font-size:18px;text-transform:uppercase}
.media-feature p{font-size:11.5px;line-height:19px;margin-top:14px}

/* projects */
.project-photo{left:0;top:2460px;width:543px;height:413px;border-radius:0 210px 210px 0;background:linear-gradient(120deg,#6d8d4a 0%,#a9c07a 40%,#e6e2d4 55%,#7d9a55 80%,#4f6b33 100%)}
.project-title{left:614px;top:2530px;font-family:"Poppins",sans-serif;font-weight:700;font-size:29px;color:var(--ink);text-transform:uppercase}
.project-text{left:618px;top:2600px;width:468px;font-size:13.5px;line-height:24px;text-align:justify;color:var(--text)}

/* blog */
.blog-card{top:3048px;width:292px;height:405px;background:var(--white);border-radius:8px;box-shadow:0 4px 18px rgba(0,0,0,.12);overflow:hidden}
.blog-photo{height:184px;background:linear-gradient(150deg,#8fa0ad,#5d6b77 50%,#a8262e)}
.blog-photo.group{background:linear-gradient(150deg,#c9b9a4,#6c7b8a 50%,#9a3a3c)}
.blog-photo.care{background:linear-gradient(150deg,#e4d3bf,#8e98b5 55%,#6a3b5a)}
.blog-body{padding:26px 24px 0}
.blog-body h4{font-family:"Poppins",sans-serif;font-weight:700;font-size:16px;line-height:20px;color:var(--ink)}
.blog-body p{font-size:12.5px;line-height:20px;color:var(--text);margin-top:10px}
.blog-arrow{width:26px;height:26px;border-radius:50%;box-shadow:0 1px 6px rgba(0,0,0,.18);margin-top:12px;display:flex;align-items:center;justify-content:center;color:var(--slate);font-size:13px}
.blog-read{position:static;width:104px;height:30px;font-size:13px;text-transform:none;margin-top:12px}

/* contact */
.contact-bg{left:0;top:3537px;width:1200px;height:800px;background:linear-gradient(180deg,#e8eef8,#dfe7f4)}
.field{background:var(--white);height:33px;font-size:11.5px;color:#555;display:flex;align-items:center;gap:7px;padding-left:14px;border:1px solid #e3e8ee}
.field.area{align-items:flex-start;padding-top:12px;height:140px}
.field svg{flex:none}
.contact-submit{left:549px;top:3955px;width:103px;height:30px;font-size:14px}

/* footer */
.footer-shape{left:0;top:4060px;width:1200px;height:499px}
.footer-brand{left:112px;top:4350px;font-family:"Poppins",sans-serif;font-weight:700;font-size:22px;line-height:26px;color:var(--white);text-transform:uppercase;display:flex;align-items:center;gap:12px}
.footer-brand .brand-mark{width:44px;height:44px}
.footer-copy{left:110px;top:4440px;font-size:14px;line-height:25px;color:var(--white)}
.footer-col{top:4322px;color:var(--white)}
.footer-col h5{font-family:"Poppins",sans-serif;font-weight:400;font-size:19px;margin-bottom:14px}
.footer-col li{list-style:none;font-size:14px;line-height:32px}
.footer-col.help li{font-size:12px}
.signup{left:816px;top:4320px;color:var(--white)}
.signup h5{font-family:"Poppins",sans-serif;font-weight:400;font-size:19px}
.signup-form{margin-top:18px;width:281px;height:40px;background:var(--white);border-radius:20px;display:flex;align-items:center;justify-content:space-between;padding-left:14px}
.signup-form span{font-size:11px;color:#333}
.signup-form b{height:40px;width:100px;border-radius:20px;background:var(--red);color:var(--white);font-weight:500;font-size:14px;display:flex;align-items:center;justify-content:center}
</style>
</head>
<body>

<!-- hero -->
<div class="abs hero-photo" role="img" aria-label="Photo of a smiling woman in a wheelchair with arms raised in a flowering meadow under a blue sky"></div>
<svg class="abs" style="left:0;top:540px" width="1200" height="260" viewBox="0 0 1200 260">
  <polygon points="0,95 600,240 1200,20 1200,260 0,260" fill="#e3f4fb"/>
  <polygon points="0,40 600,215 1200,15 1200,35 600,240 0,95" fill="#b5091c"/>
  <polygon points="1200,15 600,215 640,205 1200,0" fill="#ffffff"/>
</svg>

<header class="abs site-nav">
  <div class="abs brand"><span class="brand-mark"></span><span>Pasrel<br>Collective</span></div>
  <nav class="abs nav-links">
    <span class="active">Home</span><span>About</span><span>Our Achivement</span><span>Media</span><span>Events</span>
  </nav>
  <div class="btn nav-contact">Contact</div>
</header>

<h1 class="abs hero-title">Welcome to Pasrel<br>Collective</h1>
<p class="abs hero-text">Lorem ipsum dolor sit amet, consectetur adipiscing elit, sed do eiusmod tempor incididunt ut labore et dolore magna aliqua.</p>
<div class="btn hero-donate">Donate</div>

<!-- about -->
<svg class="abs about-bg" width="1200" height="470" viewBox="0 0 1200 470">
  <polygon points="0,0 1200,0 1200,300 600,468 0,300" fill="#e3f4fb"/>
</svg>
<h2 class="abs about-title">ABOUT US</h2>
<p class="abs about-lead">Friends living in the region who are committed to making the <b>Val des Cimes Region as accessible as possible to people indisability</b></p>
<p class="abs about-text">Sed ut perspiciatis unde omnis iste natus error sit voluptatem accusantium doloremque laudantium, totam rem aperiam, eaque ipsa quae ab illo inventore veritatis et quasi architecto beatae vitae dicta sunt explicabo. Nemo enim ipsam voluptatem quia voluptas sit aspernatur aut odit aut fugit, sed quia consequuntur magni dolores eos qui ratione voluptatem sequi nesciunt.</p>
<div class="btn about-more">Raed More</div>

<!-- achievements -->
<h2 class="section-title" style="top:1326px">Our Achievements</h2>

<div class="abs achievement" style="left:76px;top:1482px">
  <div class="icon dark"><svg width="62" height="52" viewBox="0 0 62 52"><rect x="2" y="12" width="58" height="38" rx="4" fill="#fff"/><rect x="20" y="2" width="22" height="12" rx="3" fill="none" stroke="#fff" stroke-width="4"/><rect x="2" y="22" width="58" height="4" fill="#2f3538"/><rect x="26" y="18" width="10" height="14" rx="2" fill="#2f3538"/></svg></div>
  <h3>Lorem ipsum</h3>
  <p>"Sed ut perspiciatis unde omnis iste natus error sit voluptatem accusantium doloremque laudantium</p>
</div>
<div class="abs achievement" style="left:344px;top:1440px">
  <div class="icon red"><svg width="80" height="60" viewBox="0 0 80 60"><circle cx="40" cy="12" r="10" fill="#fff"/><circle cx="18" cy="18" r="8" fill="#fff"/><circle cx="62" cy="18" r="8" fill="#fff"/><rect x="28" y="25" width="24" height="33" rx="10" fill="#fff"/><rect x="6" y="29" width="22" height="28" rx="9" fill="#fff"/><rect x="52" y="29" width="22" height="28" rx="9" fill="#fff"/></svg></div>
  <h3>Lorem ipsum</h3>
  <p>"Sed ut perspiciatis unde omnis iste natus error sit voluptatem accusantium doloremque laudantium</p>
</div>
<div class="abs achievement" style="left:611px;top:1482px">
  <div class="icon dark"><svg width="60" height="70" viewBox="0 0 60 70"><polygon points="16,38 6,64 18,60 24,70 30,46" fill="#fff"/><polygon points="44,38 54,64 42,60 36,70 30,46" fill="#fff"/><circle cx="30" cy="26" r="24" fill="#fff"/><circle cx="30" cy="26" r="14" fill="#2f3538"/><circle cx="30" cy="26" r="9" fill="#fff"/></svg></div>
  <h3>Lorem ipsum</h3>
  <p>"Sed ut perspiciatis unde omnis iste natus error sit voluptatem accusantium doloremque laudantium</p>
</div>
<div class="abs achievement" style="left:878px;top:1440px">
  <div class="icon red"><svg width="72" height="66" viewBox="0 0 72 66"><circle cx="40" cy="10" r="8" fill="#fff"/><rect x="30" y="20" width="22" height="14" rx="6" fill="#fff"/><path d="M4 34 L16 30 L30 40 L46 38 Q52 38 50 44 L36 46 L56 46 L66 38 Q72 36 70 42 L56 58 L26 60 L12 54 L4 60 Z" fill="#fff"/></svg></div>
  <h3>Lorem ipsum</h3>
  <p>"Sed ut perspiciatis unde omnis iste natus error sit voluptatem accusantium doloremque laudantium</p>
</div>

<!-- media -->
<div class="abs media-bg"></div>
<h2 class="section-title" style="top:1935px">Media</h2>
<div class="abs media-card" style="left:112px"><div class="media-photo" role="img" aria-label="Group photo of volunteers dressed as Santa Claus indoors"></div></div>
<div class="abs media-card" style="left:446px"><div class="media-photo media-feature"><h4>Lorem Ipsum</h4><p>Lorem ipsum dolor sit amet, consectetur adipiscing elit, sed do eiusmod tempor incididunt ut labore et dolore magna aliqua. Ut enim ad minim veniam,</p></div></div>
<div class="abs media-card" style="left:782px"><div class="media-photo street" role="img" aria-label="Crowd of riders in Santa costumes with motorbikes in a town street"></div></div>

<!-- projects -->
<div class="abs project-photo" role="img" aria-label="Photo of a man with a white cane walking down garden steps between columns"></div>
<h2 class="abs project-title">Association Projects</h2>
<p class="abs project-text">Promote The Reception And Leisure Of People With Disabilities In Theval des Cimes Region By Bringing Together Theinformationserved To Serve The General Interest Of People Indisability As Well As Relievecaregivers And Companions.allow Access To Leisure And Placeslike Everyone Else.raising Awareness And Developingsocial Representations, Through Actions,communications, Projects And Events Touching And Involving Partnersassociative, Economic, Political,mediaand The General Public.promote Collaboration Withlocal Actors.</p>

<!-- blog -->
<h2 class="section-title" style="top:2944px">Our Blog</h2>
<article class="abs blog-card" style="left:112px">
  <div class="blog-photo" role="img" aria-label="Photo of a man in a red shirt using a wheelchair outdoors"></div>
  <div class="blog-body"><h4>Adapt accessibility to certain places</h4><p>Lorem ipsum dolor sit amet, adipiscing elit, sed do eiusmod tempor incididunt ut labore et dolore magna aliqua. Ut enim ad minim veniam .</p><div class="blog-arrow">›</div></div>
</article>
<article class="abs blog-card" style="left:455px">
  <div class="blog-photo group" role="img" aria-label="Photo of smiling friends gathered together, one using a wheelchair"></div>
  <div class="blog-body"><h4>Mettre à disposition des interprètes pour</h4><p>Lorem ipsum dolor sit amet, adipiscing elit, sed do eiusmod tempor incididunt ut labore et dolore magna aliqua. Ut enim ad minim veniam .</p><div class="btn blog-read">Read More</div></div>
</article>
<article class="abs blog-card" style="left:797px">
  <div class="blog-photo care" role="img" aria-label="Photo of a carer assisting a child in a classroom"></div>
  <div class="blog-body"><h4>Advise various players in the sector tourism and culture</h4><p>Lorem ipsum dolor sit amet, adipiscing elit, sed do eiusmod tempor incididunt ut labore et dolore magna aliqua. Ut enim ad minim veniam .</p><div class="blog-arrow">›</div></div>
</article>

<!-- contact -->
<div class="abs contact-bg"></div>
<h2 class="section-title" style="top:3620px">Contact Us</h2>
<div class="abs field" style="left:182px;top:3717px;width:408px"><svg width="9" height="10" viewBox="0 0 9 10"><circle cx="4.5" cy="3" r="2.6" fill="#555"/><path d="M0 10 Q4.5 4 9 10Z" fill="#555"/></svg>First Name</div>
<div class="abs field" style="left:611px;top:3717px;width:408px"><svg width="9" height="10" viewBox="0 0 9 10"><circle cx="4.5" cy="3" r="2.6" fill="#555"/><path d="M0 10 Q4.5 4 9 10Z" fill="#555"/></svg>Last Name</div>
<div class="abs field" style="left:182px;top:3770px;width:408px"><svg width="11" height="9" viewBox="0 0 11 9"><rect x="0" y="3" width="11" height="6" rx="1" fill="#555"/><path d="M1 3 Q5.5 -1 10 3" stroke="#555" stroke-width="1.6" fill="none"/></svg>Telephone</div>
<div class="abs field area" style="left:611px;top:3770px;width:408px"><svg width="11" height="9" viewBox="0 0 11 9"><ellipse cx="5.5" cy="4" rx="5.5" ry="3.8" fill="#555"/><polygon points="2,6 1,9 5,7" fill="#555"/></svg>Additional Information :</div>
<div class="abs field" style="left:182px;top:3821px;width:408px"><svg width="10" height="10" viewBox="0 0 10 10"><rect x="0.5" y="0.5" width="9" height="9" rx="1.5" fill="none" stroke="#555"/><circle cx="5" cy="5" r="2" fill="#555"/></svg>Email Address</div>
<div class="abs field" style="left:182px;top:3874px;width:408px"><svg width="10" height="10" viewBox="0 0 10 10"><path d="M2 0 L4 3 L3 4 Q4 6 6 7 L7 6 L10 8 L9 10 Q2 9 0 2 Z" fill="#555"/></svg>Phone Number</div>
<div class="btn contact-submit">Submit</div>

<!-- footer -->
<svg class="abs footer-shape" width="1200" height="499" viewBox="0 0 1200 499">
  <polygon points="0,230 600,20 1200,230 1200,270 600,60 0,270" fill="#b5091c"/>
  <polygon points="0,270 600,60 1070,225 1200,250 1200,499 0,499" fill="#ffffff"/>
  <polygon points="0,300 600,95 1200,300 1200,499 0,499" fill="#050505"/>
</svg>
<div class="abs footer-brand"><span class="brand-mark"></span><span>Pasrel<br>Collective</span></div>
<p class="abs footer-copy">© 2022 Pasrel Collective |<br>All Rights Reserved</p>
<div class="abs footer-col" style="left:482px"><h5>Use Links</h5><ul><li>Home</li><li>About</li><li>Our Achivement</li><li>Media</li><li>Events</li></ul></div>
<div class="abs footer-col help" style="left:651px"><h5>Help Links</h5><ul><li>Terms &amp; condtions</li><li>Privacy Policy</li><li>Support</li></ul></div>
<div class="abs signup"><h5>Sign Up For Updates</h5><div class="signup-form"><span>Enter Email.....</span><b>Subscribe</b></div></div>

</body>
</html>
```